Kestrel Plumbing business card full re design & logo design

Kestrel Plumbing is a Sydney based mechanical plumbing contractor company.
We would like a full redesign with new logo etc which we can take to a future website, uniforms, vehicle sign writing etc.
Blue is my preferred choice of colour but i would be open to see a couple of alternatives thrown in the mix to see how they compare. I am open to see on white cards, black cards etc. Open to many new ideas.
Please see attached original business cards which have been used for the last 5 years.

Target Market(s)

Mechanical services industry.

Industry/Entity Type

Plumbing

Contact Information for Business Card

Dale Fenmore
Director

Mob: 0427 596 418
Email: dale@kestrelplumbing-demo.net.au
PO BOX 782
Harwood Vale NSW 2199
Lic: 518604k

Logo Text

Kestrel Plumbing

Font styles to use
Sans Serif

Colors
0655a3
3276b5
0792cd
33a6d7
85cae6
000000
333333
474747

Requirements
Must have
• Things that make it very professional and very well presented.
Nice to have
• Same description or very similar to attached uploaded file
Should not have
• Anything that makes it look unprofessional or cartoony.

```html
<!DOCTYPE html>
<html lang="en">
<head>
<meta charset="utf-8">
<title>Kestrel Plumbing – Business Card</title>
<link rel="stylesheet" href="https://fonts.googleapis.com/css2?family=Work+Sans:wght@300;400;500;600;700&display=swap">
<style>
  :root {
    --blue-deep: #0655a3;
    --blue-mid: #3276b5;
    --blue-bright: #0792cd;
    --blue-light: #33a6d7;
    --ink: #333333;
    --ink-soft: #474747;
    --paper: #ffffff;
    --backdrop: #2a2a2a;
  }
  * { margin: 0; padding: 0; box-sizing: border-box; }
  html, body { width: 1200px; height: 900px; overflow: hidden; }
  body {
    background: var(--backdrop);
    font-family: "Work Sans", Arial, sans-serif;
    position: relative;
  }
  .card {
    position: absolute;
    width: 620px;
    height: 354px;
    left: 290px;
    border-radius: 2px;
    overflow: hidden;
    box-shadow: 0 12px 30px rgba(0,0,0,0.45);
  }
  /* Front */
  .card-front {
    top: 60px;
    background: linear-gradient(160deg, #1565b8 0%, var(--blue-deep) 100%);
    color: var(--paper);
    text-align: center;
  }
  .brand {
    position: absolute;
    top: 62px;
    left: 0; right: 0;
    display: flex;
    justify-content: center;
    align-items: center;
    gap: 18px;
  }
  .brand-dot {
    width: 58px; height: 58px;
    border-radius: 50%;
    background: var(--paper);
  }
  .brand-name {
    font-weight: 600;
    color: var(--paper);
    text-align: left;
    line-height: 1;
  }
  .brand-name .line-1 { display: block; font-size: 44px; letter-spacing: 1px; }
  .brand-name .line-2 { display: block; font-size: 16px; letter-spacing: 15px; margin-top: 6px; }
  .front-tagline {
    position: absolute;
    top: 172px; left: 0; right: 0;
    font-size: 24px;
    font-weight: 500;
    letter-spacing: 0.5px;
  }
  .front-subhead {
    position: absolute;
    top: 212px; left: 0; right: 0;
    font-size: 18px;
    font-weight: 500;
  }
  .front-services {
    position: absolute;
    top: 252px; left: 0; right: 0;
    font-size: 15px;
    font-weight: 400;
    line-height: 1.55;
  }
  /* Back */
  .card-back {
    top: 474px;
    background: var(--paper);
    color: var(--ink);
  }
  .side-band {
    position: absolute;
    top: 0; left: 0; bottom: 0;
    width: 208px;
    background: linear-gradient(180deg, #3a8ccb 0%, var(--blue-mid) 55%, #2a6cb3 100%);
  }
  .side-brand {
    position: absolute;
    left: 50%; top: 50%;
    transform: translate(-50%, -50%) rotate(-90deg);
    display: flex;
    align-items: center;
    gap: 14px;
    white-space: nowrap;
  }
  .side-brand .brand-dot { width: 40px; height: 40px; }
  .side-brand .line-1 { font-size: 31px; }
  .side-brand .line-2 { font-size: 12px; letter-spacing: 10px; margin-top: 4px; }
  .contact {
    position: absolute;
    left: 250px; top: 44px; right: 24px;
  }
  .contact-name {
    font-size: 28px;
    font-weight: 500;
    color: var(--blue-mid);
  }
  .contact-role {
    font-size: 15px;
    font-weight: 300;
    color: var(--ink-soft);
    margin-top: 2px;
  }
  .contact-lines {
    margin-top: 36px;
    font-size: 15px;
    font-weight: 300;
    line-height: 1.4;
    color: var(--ink);
  }
  .contact-lines strong { font-weight: 500; }
  .company-label {
    margin-top: 34px;
    font-size: 16px;
    font-weight: 500;
    color: var(--blue-bright);
    letter-spacing: 0.3px;
  }
  .address {
    font-size: 15px;
    font-weight: 300;
    line-height: 1.4;
    color: var(--ink-soft);
    margin-top: 2px;
  }
</style>
</head>
<body>
  <section class="card card-front">
    <div class="brand">
      <span class="brand-dot"></span>
      <span class="brand-name"><span class="line-1">KESTREL</span><span class="line-2">PLUMBING</span></span>
    </div>
    <p class="front-tagline">MECHANICAL PLUMBING SERVICES</p>
    <p class="front-subhead">SPECIALISING IN:</p>
    <p class="front-services">Make Good | Refurbishment | Tenancy | Fit Out<br>Plant Room Works | Shut Downs | Change Overs</p>
  </section>

  <section class="card card-back">
    <div class="side-band">
      <div class="side-brand">
        <span class="brand-dot"></span>
        <span class="brand-name"><span class="line-1">KESTREL</span><span class="line-2">PLUMBING</span></span>
      </div>
    </div>
    <div class="contact">
      <h1 class="contact-name">Dale Fenmore</h1>
      <p class="contact-role">Director</p>
      <p class="contact-lines">
        <strong>Mobile:</strong> 0427 596 418<br>
        <strong>Email:</strong> dale@kestrelplumbing-demo.net.au<br>
        <strong>Lic:</strong> 518604k
      </p>
      <p class="company-label">KESTREL PLUMBING</p>
      <p class="address">P. O. Box 782<br>Harwood Vale NSW 2199</p>
    </div>
  </section>
</body>
</html>
```